Law Office business card design

I have a general practice specializing in criminal defense work and domestic cases. I have extensive trial and appellate experience.

Target Market(s)

general public

Industry/Entity Type

Defense

Contact Information for Business Card

Darrowby Law Office, P.A.
382 N. 4th
PO Box 5274
Harwick, NE 67409-5274
(555) 555-0172
(555) 555-0198 FAX
tdarrow@plinkmail.example

Requirements
Must have
• A symbol that immediately identifes the card as a legal practice.

```html
<!DOCTYPE html>
<html lang="en">
<head>
<meta charset="utf-8">
<title>Darrowby Law Office – Business Card</title>
<link href="https://fonts.googleapis.com/css2?family=Tinos:wght@400;700&display=swap" rel="stylesheet">
<style>
  :root {
    --page-bg: #e9e7e3;
    --card-bg: #ffffff;
    --ink: #1c1c1c;
    --ink-soft: #3a3a3a;
    --rule: #2a2a2a;
    --band: #2b2b2d;
  }
  * { box-sizing: border-box; margin: 0; padding: 0; }
  html, body {
    width: 1200px; height: 1023px; overflow: hidden;
    background: var(--page-bg);
    font-family: "Tinos", "Times New Roman", serif;
    color: var(--ink);
  }
  .card {
    position: absolute; left: 150px; top: 254px;
    width: 900px; height: 515px;
    background: var(--card-bg);
    box-shadow: 0 6px 18px rgba(0,0,0,.18);
  }
  .brand {
    position: absolute; left: 52px; top: 48px;
    display: flex; align-items: center; gap: 22px;
  }
  .brand-square {
    width: 168px; height: 150px;
    border: 1.5px solid var(--ink-soft);
  }
  .brand-name { line-height: 1; }
  .brand-name .firm {
    display: block; font-weight: 700; font-size: 62px; letter-spacing: 1px;
  }
  .brand-name .practice {
    display: block; font-size: 34px; letter-spacing: 9px; margin-top: 6px;
  }
  .rule-row {
    position: absolute; left: 0; right: 0; top: 268px;
    display: flex; align-items: center; gap: 18px;
  }
  .rule-row .rule { height: 1.5px; background: var(--rule); }
  .rule-row .rule-left { width: 450px; }
  .rule-row .rule-right { flex: 1; }
  .person { text-align: center; line-height: 1.05; }
  .person .name { font-weight: 700; font-size: 32px; }
  .person .title { font-size: 20px; color: var(--ink-soft); }
  .contact {
    position: absolute; left: 200px; top: 330px;
    display: flex; gap: 12px;
  }
  .contact .icons { display: flex; flex-direction: column; gap: 4px; padding-top: 3px; }
  .contact .icons svg { width: 18px; height: 18px; display: block; }
  .contact .lines { list-style: none; font-size: 19px; line-height: 22px; }
  .office {
    position: absolute; left: 600px; top: 330px;
    font-size: 19px; line-height: 23px; font-style: normal;
  }
  .office .label { font-weight: 700; }
  .bottom-edge {
    position: absolute; left: 0; right: 0; bottom: 0; height: 34px;
  }
  .bottom-edge .thin { position: absolute; left: 0; right: 0; top: 0; height: 2px; background: var(--rule); }
  .bottom-edge .band { position: absolute; left: 0; right: 0; top: 10px; bottom: 0; background: var(--band); }
</style>
</head>
<body>
  <section class="card" aria-label="Darrowby Law Office business card">
    <div class="brand">
      <div class="brand-square"></div>
      <div class="brand-name">
        <span class="firm">Darrowby</span>
        <span class="practice">Law Office</span>
      </div>
    </div>

    <div class="rule-row">
      <div class="rule rule-left"></div>
      <div class="person">
        <div class="name">Darrowby</div>
        <div class="title">Director</div>
      </div>
      <div class="rule rule-right"></div>
    </div>

    <div class="contact">
      <div class="icons" aria-hidden="true">
        <svg viewBox="0 0 18 18"><rect x="0.5" y="0.5" width="17" height="17" fill="none" stroke="#1c1c1c"/><path d="M4 9 L9 4.5 L14 9 M5.5 8 V13.5 H12.5 V8" fill="none" stroke="#1c1c1c" stroke-width="1.4"/></svg>
        <svg viewBox="0 0 18 18"><rect x="0.5" y="0.5" width="17" height="17" fill="none" stroke="#1c1c1c"/><path d="M5 4 L7.5 4 L8.5 7 L7 8 Q8.5 11 10.5 11.5 L11.5 10 L14 11 L14 13.5 Q8 14 4.5 8 Q4.3 5.5 5 4 Z" fill="#1c1c1c"/></svg>
        <svg viewBox="0 0 18 18"><rect x="0.5" y="0.5" width="17" height="17" fill="none" stroke="#1c1c1c"/><rect x="4" y="7" width="10" height="7" fill="none" stroke="#1c1c1c" stroke-width="1.3"/><rect x="6" y="3.5" width="6" height="4" fill="none" stroke="#1c1c1c" stroke-width="1.3"/></svg>
        <svg viewBox="0 0 18 18"><rect x="0.5" y="0.5" width="17" height="17" fill="none" stroke="#1c1c1c"/><rect x="3.5" y="5" width="11" height="8" fill="none" stroke="#1c1c1c" stroke-width="1.3"/><path d="M3.5 5 L9 9.5 L14.5 5" fill="none" stroke="#1c1c1c" stroke-width="1.3"/></svg>
      </div>
      <ul class="lines">
        <li>67409-5274</li>
        <li>(555) 555-0172</li>
        <li>(555) 555-0198</li>
        <li>tdarrow@plinkmail.example</li>
      </ul>
    </div>

    <address class="office">
      <div class="label">Law Office:</div>
      <div>P.A. 382 N. 4th</div>
      <div>PO Box 5274 Harwick, NE</div>
    </address>

    <div class="bottom-edge" aria-hidden="true">
      <div class="thin"></div>
      <div class="band"></div>
    </div>
  </section>
</body>
</html>
```